Home Remodeling company needs a business card design

we need a business card design for home remodeling company in hamilton county, indiana USA. we offers a wide range of construction services including whole house renovations, Design and Build Basements and Kitchen and Bathroom Remodeling . we would like to see designs for both site of business card that use the same color of the company logo and also including all information below :
1- Samir Daoudi CEO / General Contractor
2- all company contacts Telephone numbers ( 1-888-TOVAL-42 ) ( 317-555-0192) email address ( info@tovalhome.example) website ( www.tovalhome.example ) and social media logos (Facebook- twitter- google plus )
3- company logo
4- licensed . insured . bonded

```html
<!DOCTYPE html>
<html lang="en">
<head>
<meta charset="utf-8">
<title>Toval Home Remodeling – Business Card</title>
<link href="https://fonts.googleapis.com/css2?family=Roboto:wght@400;500;700&display=swap" rel="stylesheet">
<style>
  :root {
    --backdrop: #3b3431;
    --card-white: #f4f4f4;
    --charcoal: #3a3a3a;
    --ink: #333333;
    --brand-red: #d1242c;
    --on-dark: #ffffff;
    --on-dark-soft: #e2e2e2;
  }
  * { box-sizing: border-box; margin: 0; padding: 0; }
  html, body { width: 1200px; height: 716px; overflow: hidden; }
  body {
    background: var(--backdrop);
    font-family: "Roboto", Arial, sans-serif;
    position: relative;
  }
  .card {
    position: absolute;
    top: 210px;
    width: 520px;
    height: 297px;
    background: var(--card-white);
    overflow: hidden;
    box-shadow: 0 10px 24px rgba(0,0,0,.35);
  }
  .card--front { left: 40px; }
  .card--back { left: 640px; }

  .company-name {
    color: var(--ink);
    font-weight: 500;
    white-space: nowrap;
    line-height: 1;
  }
  .card--front .company-name {
    position: absolute; left: 0; right: 0; top: 50%;
    transform: translateY(-50%);
    text-align: center;
    font-size: 32px;
    letter-spacing: 1px;
  }
  .card--back .company-name {
    position: absolute; left: 46px; top: 0; height: 297px;
    display: flex; align-items: center; justify-content: center;
    writing-mode: vertical-rl;
    transform: rotate(180deg);
    font-size: 22px;
    letter-spacing: .5px;
  }

  .back__shape { position: absolute; inset: 0; }

  .contact {
    position: absolute; left: 246px; top: 56px; color: var(--on-dark);
  }
  .contact__name { font-size: 20px; font-weight: 700; letter-spacing: .5px; }
  .contact__title { font-size: 11.5px; color: var(--on-dark-soft); margin-top: 3px; margin-left: 2px; }
  .contact__list { list-style: none; margin-top: 16px; }
  .contact__item { display: flex; align-items: center; gap: 10px; font-size: 13.5px; margin-bottom: 5px; }
  .contact__icon { width: 12px; height: 12px; fill: var(--on-dark-soft); flex: none; }
  .social { display: flex; align-items: center; gap: 6px; font-size: 13.5px; margin-top: 12px; }
  .social__chip { width: 16px; height: 16px; background: var(--on-dark); border-radius: 2px; }
  .credentials { font-size: 14px; margin-top: 10px; letter-spacing: .3px; }
</style>
</head>
<body>

<section class="card card--front" aria-label="Business card front">
  <p class="company-name">Toval Home Remodeling</p>
</section>

<section class="card card--back" aria-label="Business card back">
  <svg class="back__shape" width="520" height="297" viewBox="0 0 520 297" aria-hidden="true">
    <path d="M205 0 Q175 180 92 297 L520 297 L520 0 Z" fill="var(--charcoal)"/>
    <path d="M188 0 Q158 170 66 297" fill="none" stroke="var(--brand-red)" stroke-width="4"/>
  </svg>

  <p class="company-name">Toval Home Remodeling</p>

  <div class="contact">
    <h1 class="contact__name">Samir Daoudi</h1>
    <p class="contact__title">CEO / General Contractor</p>
    <ul class="contact__list">
      <li class="contact__item">
        <svg class="contact__icon" viewBox="0 0 24 24"><path d="M6.6 10.8a15 15 0 0 0 6.6 6.6l2.2-2.2c.3-.3.7-.4 1-.2 1.1.4 2.3.6 3.6.6.6 0 1 .4 1 1V20c0 .6-.4 1-1 1A17 17 0 0 1 3 4c0-.6.4-1 1-1h3.5c.6 0 1 .4 1 1 0 1.3.2 2.5.6 3.6.1.3 0 .7-.2 1z"/></svg>
        <span>1-888-TOVAL-42</span>
      </li>
      <li class="contact__item">
        <svg class="contact__icon" viewBox="0 0 24 24"><path d="M3 8c0-2 4-4 9-4s9 2 9 4v2h-5V8H8v2H3zM6 11h12l2 9H4zm6 2a3 3 0 1 0 0 6 3 3 0 0 0 0-6z"/></svg>
        <span>317-555-0192</span>
      </li>
      <li class="contact__item">
        <svg class="contact__icon" viewBox="0 0 24 24"><path d="M2 5h20v14H2zm2 2v.5l8 5 8-5V7l-8 5z"/></svg>
        <span>info@tovalhome.example</span>
      </li>
      <li class="contact__item">
        <svg class="contact__icon" viewBox="0 0 24 24"><path d="M12 2a10 10 0 1 0 0 20 10 10 0 0 0 0-20zm0 2c1 0 2.3 2 2.8 5H9.2C9.7 6 11 4 12 4zM4.3 11h4.6a18 18 0 0 0 0 2H4.3a8 8 0 0 1 0-2zm10.8 0h4.6a8 8 0 0 1 0 2h-4.6a18 18 0 0 0 0-2zM9.2 15h5.6c-.5 3-1.8 5-2.8 5s-2.3-2-2.8-5z"/></svg>
        <span>www.tovalhome.example</span>
      </li>
    </ul>
    <div class="social">
      <span>Follows on:</span>
      <span class="social__chip" aria-label="Social profile"></span>
      <span class="social__chip" aria-label="Social profile"></span>
      <span class="social__chip" aria-label="Social profile"></span>
    </div>
    <p class="credentials">Licensed &nbsp;•&nbsp; Insured &nbsp;•&nbsp; Bonded</p>
  </div>
</section>

</body>
</html>
```